Business Cards for New Club President

I would like to get Business cards for the new president of our club. Our organization used Quillora Hub last year to create a logo for an event and we love that logo. The new president really likes the logo and would like to use it for her personal logo. But since it was created for a specific event, it needs to be modified. She would like to keep the same basic design but add a strand of pearls winding through the image.

Contact Information for Business Card

Name of President, email, phone, location

Font styles to use
Serif

Colors
ec1f27
fff4ee

Requirements
Must have
• 1. A modified version of the image we previously purchased from Quillora Hub. (see uploaded image); remove the name of the event and date..
2. A strand of pearls (or individual pearls) gracefully wrapping through the image.
3. The phrase "Kestrelvale Alumnae" or "Kestrelvale Alumnae Chapter" on the design
Nice to have
• Use the original design we purchased from Quillora Hub
Should not have
• Should not have any other colors other than red, white or black.

```html
<!DOCTYPE html>
<html lang="en">
<head>
<meta charset="UTF-8">
<title>Kestrelvale Alumnae Chapter – Business Cards</title>
<link rel="stylesheet" href="https://fonts.googleapis.com/css2?family=Oswald:wght@500&family=Work+Sans:wght@400;500&display=swap">
<style>
  :root {
    --bg: #e9e6e3;
    --card: #111112;
    --card-deep: #050505;
    --red: #ec1f27;
    --white: #fff4ee;
    --silver: #b9b9b9;
    --silver-dark: #6d6d6d;
  }
  * { box-sizing: border-box; margin: 0; padding: 0; }
  html, body { width: 1200px; height: 716px; overflow: hidden; }
  body { background: var(--bg); position: relative; }

  .card {
    position: absolute;
    top: 198px;
    width: 560px;
    height: 320px;
    background: var(--card);
    border-radius: 6px;
    overflow: hidden;
    box-shadow: 0 10px 30px rgba(0,0,0,.25);
  }
  .card--front { left: 27px; background: var(--card-deep); }
  .card--back { left: 613px; }

  .chapter-title {
    position: absolute;
    left: 36px;
    top: 62px;
    font-family: "Oswald", sans-serif;
    font-weight: 500;
    font-size: 20px;
    letter-spacing: .5px;
    color: var(--white);
    text-transform: uppercase;
  }

  .artwork { position: absolute; }
  .artwork--front {
    left: 250px; top: 0; width: 310px; height: 320px;
    background: linear-gradient(115deg, transparent 0%, rgba(40,40,40,.6) 30%, var(--silver-dark) 55%, var(--silver) 80%, #8e8e8e 100%);
    clip-path: polygon(40% 100%, 100% 0, 100% 100%);
  }
  .artwork--back {
    left: 0; top: 0; width: 300px; height: 320px;
    background: linear-gradient(100deg, var(--silver) 0%, #8a8a8a 35%, #2a2a2a 70%, transparent 100%);
    clip-path: polygon(0 0, 30% 0, 60% 100%, 0 100%);
  }

  .brand {
    position: absolute;
    right: 48px;
    top: 70px;
    display: flex;
    align-items: center;
    gap: 8px;
    font-family: "Work Sans", sans-serif;
    font-weight: 500;
    font-size: 17px;
    color: var(--red);
  }
  .brand-dot { width: 12px; height: 12px; border-radius: 50%; background: var(--red); }

  .identity {
    position: absolute;
    right: 48px;
    top: 122px;
    text-align: right;
    font-family: "Work Sans", sans-serif;
  }
  .identity-name {
    font-size: 26px;
    font-weight: 400;
    color: var(--red);
    text-transform: uppercase;
    letter-spacing: .5px;
  }
  .identity-role { font-size: 14px; color: var(--white); margin-top: 2px; }

  .contact {
    position: absolute;
    right: 48px;
    top: 200px;
    list-style: none;
    font-family: "Work Sans", sans-serif;
    font-size: 13.5px;
    color: var(--white);
    text-align: right;
    line-height: 19px;
  }
  .contact li { display: flex; justify-content: flex-end; align-items: center; gap: 7px; }
  .contact svg { width: 10px; height: 10px; fill: none; stroke: var(--red); stroke-width: 1.6; }
  .contact .no-icon { padding-right: 17px; }

  .accent-bar {
    position: absolute;
    right: 0;
    top: 168px;
    width: 6px;
    height: 28px;
    background: var(--red);
  }
</style>
</head>
<body>

  <section class="card card--front" aria-label="Card front">
    <h1 class="chapter-title">Kestrelvale Alumnae Chapter</h1>
    <div class="artwork artwork--front" role="img" aria-label="Embossed silver illustration of hibiscus flowers, waves and a temple roof"></div>
  </section>

  <section class="card card--back" aria-label="Card back">
    <div class="artwork artwork--back" role="img" aria-label="Embossed silver illustration of hibiscus flowers, leaves, waves and a pagoda"></div>

    <div class="brand"><span class="brand-dot"></span>Kestrelvale Alumnae</div>

    <div class="identity">
      <h2 class="identity-name">Dorian Vell</h2>
      <p class="identity-role">Director</p>
    </div>

    <ul class="contact">
      <li class="no-icon">418 Lindcrest Lane</li>
      <li class="no-icon">Fairholm, CA 90417</li>
      <li>043 555 01 27
        <svg viewBox="0 0 10 10" aria-hidden="true"><path d="M2 1 L4 3 L3 4 Q4.5 6 6 7 L7 6 L9 8 L8 9 Q3 8.5 1 2 Z"/></svg>
      </li>
      <li>info@HarborClubHQ.com
        <svg viewBox="0 0 10 10" aria-hidden="true"><rect x="1" y="2" width="8" height="6"/><path d="M1 2 L5 5.5 L9 2"/></svg>
      </li>
      <li>www.HarborClubHQ.com
        <svg viewBox="0 0 10 10" aria-hidden="true"><circle cx="5" cy="5" r="4"/><path d="M1 5 H9 M5 1 Q2.5 5 5 9 M5 1 Q7.5 5 5 9"/></svg>
      </li>
    </ul>

    <span class="accent-bar"></span>
  </section>

</body>
</html>
```